A hand soap seller needs a premium label for a new product

We need a premium label for a bottle of soap. We want to write on it:
VANTROSELLA (Name)
Hypoallergenic and antibacterial hand soap
350 ml e / 11.8 fl oz (volume, http://pimaxo.ru/7K3RtWbqmeL519)
Saint Petersburg - Russia / www.vantrosella.ru
We want to see the face of a hippopotamus in the design. Use only black and white and green for accents (the color of grass). Examples of a hippopotamus are shown in the photo. Our soap is hypoallergenic. Ideal for both children and adults. Therefore, the label should appeal to adults and children.
The bottle will be white, and the soap dispenser will be black.
So I'm attaching an example of a soap design that we liked
Label size: height-78 mm, width-102 mm !!!

Target Market(s)

Mothers and children

Industry/Entity Type

Hand soap

Font styles to use
Serif

Colors

Designer to choose only greyscale colors for use in the design.

Requirements
Must have
• The face of a hippopotamus emerging from the grass, Black and white palette with elements of green (grass color)
Nice to have
• The face of a hippopotamus emerging from the grass
Should not have
• Different colors

```html
<!DOCTYPE html>
<html lang="en">
<head>
<meta charset="utf-8">
<title>Vantrosella Hand Soap Label</title>
<link rel="stylesheet" href="https://fonts.googleapis.com/css2?family=Cormorant+Garamond:wght@500;600&family=Josefin+Sans:wght@400&display=swap">
<style>
  :root {
    --ink: #0b0b0b;
    --paper: #ffffff;
    --grass: #1f8f3e;
    --canvas: #ffffff;
    --placeholder-light: #f2f2f2;
    --placeholder-mid: #d9d9d9;
  }
  html, body {
    margin: 0;
    width: 1200px;
    height: 1200px;
    overflow: hidden;
    background: var(--canvas);
  }
  .label {
    position: absolute;
    left: 70px;
    top: 195px;
    width: 1060px;
    height: 810px;
    background: var(--paper);
    border: 2px solid var(--ink);
    box-sizing: border-box;
    overflow: hidden;
    font-family: "Cormorant Garamond", serif;
    color: var(--ink);
  }
  .label__art {
    position: absolute;
    inset: 0;
    width: 100%;
    height: 100%;
  }
  .brand-band {
    position: absolute;
    left: 382px;
    top: 0;
    width: 294px;
    height: 402px;
    background: var(--ink);
  }
  .brand-name {
    position: absolute;
    left: 382px;
    top: 78px;
    width: 294px;
    box-sizing: border-box;
    padding: 0 16px;
    text-align: center;
    white-space: nowrap;
    color: var(--paper);
    font-family: "Cormorant Garamond", serif;
    font-weight: 600;
    font-size: 31px;
    line-height: 1;
    letter-spacing: 1px;
  }
  .product-name {
    position: absolute;
    left: 280px;
    top: 560px;
    width: 500px;
    text-align: center;
    font-size: 36px;
    font-weight: 600;
    line-height: 45px;
    letter-spacing: 1.5px;
    margin: 0;
  }
  .product-name__type {
    display: block;
    font-family: "Josefin Sans", sans-serif;
    font-weight: 400;
    font-size: 34px;
    letter-spacing: 0.5px;
    line-height: 44px;
  }
  .volume {
    position: absolute;
    left: 380px;
    top: 719px;
    width: 294px;
    height: 91px;
    background: var(--ink);
    color: var(--paper);
    display: flex;
    align-items: center;
    justify-content: center;
    font-size: 25px;
    font-weight: 600;
    letter-spacing: 1px;
  }
  .origin {
    position: absolute;
    left: 765px;
    top: 690px;
    font-style: normal;
    font-size: 23px;
    font-weight: 600;
    line-height: 31px;
    letter-spacing: 1px;
  }
  .origin__web {
    display: block;
    font-family: "Josefin Sans", sans-serif;
    font-weight: 400;
    color: var(--grass);
    letter-spacing: 0;
    margin-top: 2px;
  }
</style>
</head>
<body>
  <main class="label">
    <div class="brand-band"></div>
    <div class="brand-name">VANTROSELLA</div>

    <svg class="label__art" viewBox="0 0 986 753" preserveAspectRatio="none">
      <defs>
        <linearGradient id="hippoTone" x1="0" y1="0" x2="0" y2="1">
          <stop offset="0" stop-color="#f2f2f2"/>
          <stop offset="1" stop-color="#d9d9d9"/>
        </linearGradient>
      </defs>
      <path class="wave wave--upper" d="M0 405 C70 440 110 460 170 455 C240 450 290 380 350 378 C440 375 520 455 580 450 C640 445 690 390 750 392 C820 395 860 450 980 462"
            fill="none" stroke="#0b0b0b" stroke-width="14"/>
      <path class="wave wave--lower" d="M0 440 C40 470 70 505 130 505 C200 505 250 430 320 430 C400 430 460 515 520 512 C590 508 640 430 720 428 C800 426 880 500 986 505"
            fill="none" stroke="#0b0b0b" stroke-width="7"/>
      <rect class="hero-illustration" x="405" y="232" width="260" height="218" rx="40"
            fill="url(#hippoTone)" role="img"
            aria-label="Line illustration of a hippopotamus head emerging from water with a small green flower on its head"/>
    </svg>

    <h1 class="product-name">
      Hypoallergenic<br>and antibacterial
      <span class="product-name__type">HAND SOAP</span>
    </h1>

    <div class="volume">350 ml ℮ / 11.8 fl oz</div>

    <address class="origin">
      Saint Petersburg<br>Russia
      <span class="origin__web">www.vantrosella.ru</span>
    </address>
  </main>
</body>
</html>
```